Garnett and Lyle Personal Injury Billboard

We'd like a clean/modern billboard to build brand awareness for our law firm in the area of personal injury. Ideally, we like the word "Injured?" or something similar in large lettering.

I'm attaching images, logo and award badges which could be used. The billboards will be 14x48 ft and 10.6x36.

We are open to different color ideas, fonts, and artwork. Creative but not too busy with wording. Our web page is www.kgarnettfirm.example

Garnett & Lyle Law Firm
(555) 318-4092

```html
<!DOCTYPE html>
<html lang="en">
<head>
<meta charset="utf-8">
<title>Garnett &amp; Lyle Law Firm – Injured? Billboard</title>
<link href="https://fonts.googleapis.com/css2?family=Montserrat:wght@600;700;800&family=Exo+2:ital,wght@1,900&family=Barlow+Condensed:ital,wght@1,600&display=swap" rel="stylesheet">
<style>
  :root {
    --page-bg: #e8ebee;
    --board-bg: #262628;
    --board-wave: #333335;
    --band-blue-1: #1f86c9;
    --band-blue-2: #1a9ab5;
    --orange-top: #ffcf2a;
    --orange-bottom: #ff8500;
    --white: #ffffff;
    --ink: #1d1d1f;
    --icon-blue: #1f86c9;
    --photo-1: #4a5a7a;
    --photo-2: #8c95a6;
    --badge: #2a78b8;
  }
  * { margin: 0; padding: 0; box-sizing: border-box; }
  html, body {
    width: 1200px; height: 962px; overflow: hidden;
    background: var(--page-bg);
  }
  .billboard {
    position: absolute; left: 40px; top: 323px;
    width: 1120px; height: 315px;
    background: var(--board-bg);
    overflow: hidden;
  }
  .billboard__waves { position: absolute; inset: 0; }
  .attorneys-photo {
    position: absolute; left: 814px; top: 60px; width: 306px; height: 255px;
    background: linear-gradient(135deg, var(--photo-1), var(--photo-2));
  }
  .top-band { position: absolute; inset: 0; }
  .firm-name {
    position: absolute; left: 205px; width: 719px; top: 14px;
    text-align: center;
    font-family: "Montserrat", sans-serif; font-weight: 800;
    font-size: 41px; line-height: 1.1; letter-spacing: 0.3px; color: var(--white);
  }
  .headline {
    position: absolute; left: 56px; top: 86px;
    font-family: "Exo 2", sans-serif; font-style: italic; font-weight: 900;
    font-size: 108px; line-height: 1; letter-spacing: 8px;
    background: linear-gradient(180deg, var(--orange-top) 20%, var(--orange-bottom) 85%);
    -webkit-background-clip: text; background-clip: text; color: transparent;
  }
  .tagline {
    position: absolute; left: 52px; top: 186px;
    font-family: "Barlow Condensed", sans-serif; font-style: italic; font-weight: 600;
    font-size: 43px; line-height: 1; color: var(--white); letter-spacing: -0.3px;
  }
  .contact-phone {
    position: absolute; left: 86px; top: 260px; width: 340px; height: 46px;
    border: 2px solid var(--white); border-radius: 23px;
    display: flex; align-items: center;
  }
  .contact-phone__icon {
    width: 46px; height: 46px; margin-left: -2px; border-radius: 50%;
    background: var(--white); display: flex; align-items: center; justify-content: center;
  }
  .contact-phone__number {
    margin-left: 20px;
    font-family: "Montserrat", sans-serif; font-weight: 700;
    font-size: 31px; color: var(--white);
  }
  .contact-web {
    position: absolute; left: 410px; top: 260px; width: 458px; height: 46px;
    background: var(--white); border-radius: 23px;
    display: flex; align-items: center; justify-content: space-between;
    padding: 0 16px 0 34px;
  }
  .contact-web__url {
    font-family: "Montserrat", sans-serif; font-weight: 700;
    font-size: 24px; color: var(--ink);
  }
  .firm-mark {
    position: absolute; left: 878px; top: 264px; width: 104px;
    font-family: "Montserrat", sans-serif; font-weight: 700;
    font-size: 16px; line-height: 1.15; color: var(--white);
  }
  .award-badge {
    position: absolute; left: 997px; top: 260px; width: 36px; height: 46px;
    background: var(--badge);
  }
</style>
</head>
<body>
  <main class="billboard">
    <svg class="billboard__waves" width="1120" height="315" viewBox="0 0 1120 315" aria-hidden="true">
      <path d="M620 315 C700 230 820 180 1120 170 L1120 315 Z" fill="var(--board-wave)"/>
      <path d="M0 80 C60 50 120 70 140 120 C90 110 40 120 0 150 Z" fill="var(--board-wave)" opacity="0.6"/>
    </svg>

    <div class="attorneys-photo" role="img" aria-label="Portrait photo of the two founding attorneys in suits"></div>

    <svg class="top-band" width="1120" height="315" viewBox="0 0 1120 315" aria-hidden="true">
      <defs>
        <linearGradient id="bandGrad" x1="0" x2="1" y1="0" y2="0">
          <stop offset="0" stop-color="var(--band-blue-1)"/>
          <stop offset="1" stop-color="var(--band-blue-2)"/>
        </linearGradient>
      </defs>
      <path d="M0 0 H1120 V22 H950 C935 22 930 30 924 45 C918 60 910 66 895 66 H235 C220 66 212 60 206 45 C200 30 195 22 180 22 H0 Z" fill="url(#bandGrad)"/>
    </svg>

    <h1 class="firm-name">GARNETT &amp; LYLE LAW FIRM</h1>
    <p class="headline">INJURED ?</p>
    <p class="tagline">WE FIGHT FOR YOUR RIGHTS!</p>

    <div class="contact-phone">
      <span class="contact-phone__icon">
        <svg width="22" height="22" viewBox="0 0 24 24" aria-hidden="true">
          <path d="M6.6 10.8a15.1 15.1 0 0 0 6.6 6.6l2.2-2.2c.3-.3.7-.4 1-.2 1.1.4 2.300.6 3.6.6.6 0 1 .4 1 1V20c0 .6-.4 1-1 1C10.6 21 3 13.4 3 4c0-.6.4-1 1-1h3.5c.6 0 1 .4 1 1 0 1.3.2 2.5.6 3.6.1.3 0 .7-.2 1L6.6 10.8z" fill="var(--icon-blue)"/>
        </svg>
      </span>
      <span class="contact-phone__number">(555) 318-4092</span>
    </div>

    <div class="contact-web">
      <span class="contact-web__url">www.kgarnettfirm.example</span>
      <svg width="28" height="28" viewBox="0 0 24 24" aria-hidden="true">
        <circle cx="10" cy="10" r="6.5" fill="none" stroke="var(--icon-blue)" stroke-width="2.5"/>
        <line x1="14.8" y1="14.8" x2="21" y2="21" stroke="var(--icon-blue)" stroke-width="2.8" stroke-linecap="round"/>
      </svg>
    </div>

    <p class="firm-mark">Garnett &amp; Lyle</p>
    <div class="award-badge" aria-hidden="true"></div>
  </main>
</body>
</html>
```